Website for "Bright Meadow Ltd" cleaning bsuiness

We require a website to expose our business to the local market. We want to provide background on who we are and what we do but in an easily digestible way. We clean domestic and commercial premises and want to provide a list of all of our services to potential customers. We operate out of Warrington in the UK.

We would like the website to be animated in some way so that the experience of using it is not dull or mundane. This website needs to be an extension of our company.

Target Market(s)

30 - 60 year olds for Domestic plus commercial clients

Industry/Entity Type

Cleaning Service

Coding

Coded - Design and coding required

Number of Pages Required

4 page

Font styles to use
Sans Serif

Colors
0455a3
3176b5
85acd3
cfdeed
ffffff
000000
1b1b1b
c8c8c8
757575

Requirements
Must have
• Logo which has been provided. Theme based around the logo and its colours. Simple layout to avoid confusion.
Nice to have
• Animations where possible to impress the customer.
Should not have
• any pictures of cleaning equipment, fairies, maids etc

```html
<!DOCTYPE html>
<html lang="en">
<head>
<meta charset="utf-8">
<title>Bright Meadow Ltd – Professional Cleaning Services</title>
<link rel="stylesheet" href="https://fonts.googleapis.com/css2?family=Raleway:wght@400;500;600;700&family=PT+Sans:wght@400;700&display=swap">
<style>
:root{
  --blue-deep:#0455a3;
  --blue:#3176b5;
  --blue-soft:#85acd3;
  --blue-pale:#cfdeed;
  --white:#ffffff;
  --black:#000000;
  --ink:#1b1b1b;
  --grey-light:#c8c8c8;
  --grey:#757575;
}
*{margin:0;padding:0;box-sizing:border-box}
html,body{width:1200px;height:2691px;overflow:hidden}
body{position:relative;font-family:"PT Sans",Arial,sans-serif;color:var(--white);background:var(--white)}
.section{position:absolute;left:0;width:1200px;overflow:hidden}
.bg{position:absolute;inset:0}
.center{position:absolute;left:0;width:1200px;text-align:center}
.heading{font-family:"Raleway",Arial,sans-serif;font-weight:500;font-size:50px;letter-spacing:0.5px;line-height:1}
.lead{font-size:11.5px;line-height:24px;color:var(--white)}
.pill{position:absolute;display:flex;align-items:center;justify-content:center;border-radius:25px;font-family:"Raleway",Arial,sans-serif;font-weight:600;font-size:15px;width:164px;height:48px}

/* header */
.site-header{top:0;height:149px;background:var(--white)}
.brand{position:absolute;left:111px;top:54px;display:flex;align-items:center;gap:10px;color:var(--blue-deep);font-family:"PT Sans",Arial,sans-serif;font-weight:700;font-size:24px}
.brand-dot{width:18px;height:18px;border-radius:50%;background:var(--blue-deep)}
.nav-active-band{position:absolute;left:553px;top:0;width:82px;height:149px;background:var(--blue-pale)}
.nav a{position:absolute;top:59px;height:36px;line-height:36px;font-size:12.5px;color:var(--ink);text-decoration:none;font-family:"PT Sans",Arial,sans-serif}
.nav a.active{left:553px;width:82px;text-align:center;background:var(--blue-deep);color:var(--white)}

/* hero */
.hero{top:149px;height:540px}
.hero .bg{background:linear-gradient(160deg,#2e3742 0%,#46505d 45%,#3a424d 100%)}
.hero-title{top:211px;color:var(--blue);font-size:51px;font-weight:500}
.hero-text{top:282px}
.hero .pill{left:518px;top:355px;background:var(--blue);color:var(--white)}
.arrow{position:absolute;top:247px}

/* who we are */
.who{top:689px;height:579px}
.who .bg{background:linear-gradient(180deg,#1d5ba8 0%,#2a6cb6 55%,#1f5ca8 100%)}
.who-title{top:157px;color:var(--white)}
.who-text1{top:220px}
.who-tagline{top:279px;font-weight:700;font-size:13.5px}
.who-rule{position:absolute;left:456px;top:303px;width:287px;height:1px;background:var(--white)}
.who-text2{top:322px}
.who .pill{left:518px;top:389px;background:var(--white);color:var(--blue-deep)}

/* what we do */
.services{top:1268px;height:637px}
.services .bg{background:linear-gradient(170deg,#182029 0%,#2a3440 55%,#1e2630 100%)}
.services-title{top:127px;color:var(--white)}
.services-text{top:192px}
.service-card{position:absolute;top:282px;width:302px;height:239px;background:var(--white)}
.service-photo{position:absolute;left:20px;top:21px;width:262px;height:153px}
.service-name{position:absolute;left:0;top:193px;width:302px;text-align:center;font-family:"Raleway",Arial,sans-serif;font-weight:700;font-size:15.5px;color:var(--blue-deep)}

/* contact */
.contact{top:1905px;height:696px}
.contact .bg{background:linear-gradient(165deg,#2b6bb3 0%,#3479c1 50%,#2c6db6 100%)}
.contact-title{top:147px;color:var(--white)}
.contact-text{top:212px}
.detail{position:absolute;left:141px;width:420px;display:flex;align-items:center}
.detail-icon{width:62px;height:62px;border-radius:50%;background:var(--ink);display:flex;align-items:center;justify-content:center;flex:none}
.detail-text{margin-left:14px;font-size:13px;line-height:24px}
.send-label{position:absolute;left:614px;top:298px;font-family:"Raleway",Arial,sans-serif;font-weight:500;font-size:15px}
.field{position:absolute;border:1px solid var(--white);font-size:11px;padding:18px 0 0 21px;color:var(--white)}
.submit{position:absolute;left:614px;top:529px;width:473px;height:54px;background:var(--ink);font-family:"Raleway",Arial,sans-serif;font-weight:600;font-size:15px;display:flex;align-items:center;justify-content:center}

/* footer */
.site-footer{top:2601px;height:90px;background:var(--ink)}
.copyright{position:absolute;left:111px;top:38px;font-size:11.5px}
.social{position:absolute;left:988px;top:34px;display:flex;gap:7px}
.social span{width:21px;height:21px;background:var(--blue)}
.social span.alt{background:#d24a3a}
</style>
</head>
<body>

<header class="section site-header">
  <div class="brand"><span class="brand-dot"></span>Bright Meadow Ltd</div>
  <div class="nav-active-band"></div>
  <nav class="nav">
    <a class="active" href="#">HOME</a>
    <a href="#" style="left:678px">ABOUT ME</a>
    <a href="#" style="left:804px">SERVICES</a>
    <a href="#" style="left:920px">NEWS</a>
    <a href="#" style="left:1019px">CONTACT US</a>
  </nav>
</header>

<section class="section hero">
  <div class="bg" role="img" aria-label="Upward view of glass office towers against the sky"></div>
  <svg class="arrow" style="left:38px" width="24" height="46" viewBox="0 0 24 46"><polyline points="22,2 2,23 22,44" fill="none" stroke="#c8c8c8" stroke-width="1.5"/></svg>
  <svg class="arrow" style="left:1138px" width="24" height="46" viewBox="0 0 24 46"><polyline points="2,2 22,23 2,44" fill="none" stroke="#c8c8c8" stroke-width="1.5"/></svg>
  <h1 class="center heading hero-title">PROFESSIONAL CLEANING SERVICES</h1>
  <p class="center lead hero-text">Sed hendrerit justo nec facilisis congue. Ut gravida hendrerit massa non tempus. Sed et quam ut mi ultricies malesuada. Etiam porttitor nunc at nisi iaculis, vitae<br>gravida turpis tempus. Etiam velit quam, fringilla ac metus sed, convallis posuere dui.</p>
  <a class="pill">READ MORE</a>
</section>

<section class="section who">
  <div class="bg" role="img" aria-label="Aerial view of a city skyline tinted blue"></div>
  <h2 class="center heading who-title">WHO WE ARE</h2>
  <p class="center lead who-text1">Etiam sollicitudin urna sit amet posuere commodo. Nunc convallis nibh purus, ac congue urna rutrum ut. Aenean fringilla convallis urna ut mollis. Mauris lobortis<br>nisi in consequat suscipit. Donec interdum mi id ex ullamcorper vestibulum. Mauris dignissim magna vel ex porta, nec malesuada justo feugiat.</p>
  <p class="center who-tagline">We are&nbsp; cleaning services company in Warrington, UK</p>
  <div class="who-rule"></div>
  <p class="center lead who-text2">Donec viverra faucibus nibus eleifend. Ut dignissim, ante at auctor consequat, purus massa blandit nisl, nec blandit odio enim non magna. Fusce dapibus enim odio, ut<br>pellentesque sem fringilla ac. Sed scelerisque sapien lacinia, ultrices tortor sit amet, rhoncus nisl. Quisque hendrerit tempus libero eget pulvinar.</p>
  <a class="pill">READ MORE</a>
</section>

<section class="section services">
  <div class="bg" role="img" aria-label="Modern building exterior at dusk"></div>
  <h2 class="center heading services-title">WHAT WE DO</h2>
  <p class="center lead services-text">Nam id nisi commodo turpis aliquam convallis non vel ante. Morbi iaculis elit ac aliquet bibendum. Aenean elementum suscipit varius. Donec quis nibh quis nunc<br>rhoncus congue non vel mi. Mauris velit dolor, lobortis ut purus ac, tristique dapibus velit. Vivamus dapibus sapien tempus euismod vehicula.</p>
  <div class="service-card" style="left:111px">
    <div class="service-photo" role="img" aria-label="Modern apartment block with balconies" style="background:linear-gradient(180deg,#3d7cc8 0%,#6a9fd6 40%,#b86a4e 75%,#8a5a44 100%)"></div>
    <div class="service-name">MAURIS QUIS EX ORNARE</div>
  </div>
  <div class="service-card" style="left:449px">
    <div class="service-photo" role="img" aria-label="Detached family house at twilight" style="background:linear-gradient(180deg,#3f5a86 0%,#7b87a0 45%,#c9b89a 70%,#5f7a3e 100%)"></div>
    <div class="service-name">AENEAN ELEMENTUM SUSCIPIT</div>
  </div>
  <div class="service-card" style="left:786px">
    <div class="service-photo" role="img" aria-label="Residential building with balconies under blue sky" style="background:linear-gradient(180deg,#4a86cf 0%,#d9c6a4 45%,#c4ad86 75%,#5d7f4a 100%)"></div>
    <div class="service-name">SUSPENDISSE EST ENIM</div>
  </div>
</section>

<section class="section contact">
  <div class="bg" role="img" aria-label="Hand writing with a pen, tinted blue"></div>
  <h2 class="center heading contact-title">CONTACT</h2>
  <p class="center lead contact-text">Vestibulum egestas, arcu vel congue auctor, est turpis cursus felis, vel euismod magna ante at dui. Donec rhoncus sapien nec leo accumsan suscipit. Sed non ligula nec sapien<br>Sed egestas, ipsum et ultricies dapibus, erat orci euismod arcu, sit amet dignissim felis neque sed velit. Nulla ex enim, tincidun.</p>

  <div class="detail" style="top:294px">
    <div class="detail-icon"><svg width="18" height="24" viewBox="0 0 18 24"><path d="M9 0C4 0 0 4 0 9c0 6.5 9 15 9 15s9-8.5 9-15c0-5-4-9-9-9zm0 12.5A3.5 3.5 0 1 1 9 5.5a3.5 3.5 0 0 1 0 7z" fill="#fff"/></svg></div>
    <div class="detail-text">Bright Meadow<br>17 Lorem Ipsm, Lorem Ipsm, Warrington, UK 94500</div>
  </div>
  <div class="detail" style="top:387px">
    <div class="detail-icon"><svg width="20" height="20" viewBox="0 0 24 24"><path d="M6.6 10.8a15.2 15.2 0 0 0 6.6 6.6l2.2-2.2c.3-.3.7-.4 1-.2 1.1.4 2.3.6 3.6.6.6 0 1 .4 1 1V20c0 .6-.4 1-1 1C10.6 21 3 13.4 3 4c0-.6.4-1 1-1h3.5c.6 0 1 .4 1 1 0 1.3.2 2.5.6 3.6.1.3 0 .7-.2 1L6.6 10.8z" fill="#fff"/></svg></div>
    <div class="detail-text">1-425- 555-0147</div>
  </div>
  <div class="detail" style="top:479px">
    <div class="detail-icon"><svg width="20" height="15" viewBox="0 0 20 15"><path d="M0 0h20v15H0z" fill="#fff"/><path d="M0 0l10 8 10-8" fill="none" stroke="#1b1b1b" stroke-width="1.6"/></svg></div>
    <div class="detail-text">info@brightmeadow.example</div>
  </div>

  <div class="send-label">SEND MAIL</div>
  <div class="field" style="left:614px;top:343px;width:224px;height:52px">Name</div>
  <div class="field" style="left:863px;top:343px;width:224px;height:52px">Email Address</div>
  <div class="field" style="left:614px;top:420px;width:473px;height:83px;padding-top:12px">Message</div>
  <div class="submit">SUBMIT</div>
</section>

<footer class="section site-footer">
  <div class="copyright">© 2016 Bright Meadow. All rights reserved</div>
  <div class="social"><span></span><span></span><span></span><span class="alt"></span></div>
</footer>

</body>
</html>
```